Business Card Design For DJ Company

I'm rebranding my wedding and event dj company. I am looking for a modern, luxury, & fun design to match my new logo and website design. Please see attached logo and new webpage design. Colors should match. Design should flow with logo and website for recognition. I want to attract young adults. I plan on printing metallic finish cards so please keep hat in mind.

Target Market(s)

Millennials

Contact Information for Business Card

Name: Dario Colvento
Company: Cedar Hollow Mix DJ
Services: DJ – Photo Booth – Event Lighting – LED Robot

Website: www.cedarhollowmixdj.example
Email: dario@cedarhollowmixdj.example
Phone: (555)417-9382

Instagram: @chmixdj
Facebook: @chmixdj
Twitter - @chmixdj

Se Habla Español

Font styles to use
Serif
Sans Serif

Colors

Designer to choose colors to be used in the design.

Requirements
Nice to have
• Transparent Gradient background - Image related to weddings

```html
<!DOCTYPE html>
<html lang="en">
<head>
<meta charset="utf-8">
<title>Cedar Hollow Mix DJ — Business Card</title>
<link rel="stylesheet" href="https://fonts.googleapis.com/css2?family=Lato:wght@400;700&family=Michroma&display=swap">
<style>
  :root {
    --bg: #2b2b2d;
    --card: #1f2022;
    --card-back: #1c1d1f;
    --pattern: #242527;
    --orange: #f7941d;
    --green: #8dc63f;
    --blue: #29a8e0;
    --text: #f2f2f2;
    --rule: #6d6e70;
  }
  * { margin: 0; padding: 0; box-sizing: border-box; }
  html, body { width: 1200px; height: 1108px; overflow: hidden; background: var(--bg); }
  .stage { position: relative; width: 1200px; height: 1108px; }
  .card {
    position: absolute; top: 194px; width: 440px; height: 720px;
    border-radius: 22px; overflow: hidden;
    font-family: "Lato", sans-serif; color: var(--text);
  }
  .card--front { left: 120px; background: var(--card); }
  .card--back { left: 640px; background: var(--card-back); }

  .brand {
    position: absolute; top: 90px; left: 50%; transform: translateX(-50%);
    width: 260px; height: 260px; border-radius: 50%;
    border: 8px solid var(--blue);
    display: flex; align-items: center; justify-content: center; text-align: center;
  }
  .brand__name {
    font-family: "Lato", sans-serif; font-weight: 700; font-size: 30px;
    line-height: 1.15; color: var(--orange); letter-spacing: 1px; text-transform: uppercase;
  }

  .holder {
    position: absolute; top: 420px; width: 100%; text-align: center;
    font-family: "Michroma", sans-serif; font-size: 21px; letter-spacing: 0.5px;
  }
  .holder__first { color: var(--orange); }
  .holder__last { color: var(--green); }

  .divider {
    position: absolute; left: 60px; right: 60px; height: 24px;
    display: flex; align-items: center; gap: 10px;
  }
  .divider::before, .divider::after { content: ""; flex: 1; height: 1px; background: var(--rule); }
  .divider--contact { top: 470px; }
  .divider--social { top: 622px; }
  .icon-row { display: flex; gap: 5px; }
  .icon-row svg { width: 22px; height: 22px; display: block; }

  .contact {
    position: absolute; top: 504px; width: 100%; text-align: center;
    font-size: 18px; line-height: 27px; color: var(--text);
  }
  .handle {
    position: absolute; top: 654px; width: 100%; text-align: center;
    font-size: 18px; color: var(--text);
  }

  .back-pattern {
    position: absolute; inset: 0;
    background: radial-gradient(circle at 50% 40%, var(--pattern), var(--card-back) 75%);
  }
  .services {
    position: absolute; bottom: 95px; width: 100%; text-align: center;
    font-size: 19px; line-height: 25px; text-transform: uppercase; color: var(--text);
  }
</style>
</head>
<body>
<main class="stage">
  <section class="card card--front">
    <div class="brand">
      <span class="brand__name">Cedar Hollow<br>Mix DJ</span>
    </div>

    <p class="holder"><span class="holder__first">DARIO</span> <span class="holder__last">COLVENTO</span></p>

    <div class="divider divider--contact">
      <div class="icon-row">
        <svg viewBox="0 0 22 22" aria-label="phone"><circle cx="11" cy="11" r="10" fill="none" stroke="var(--blue)" stroke-width="2"/><path d="M8 6.5l2 2-1 1.2c.6 1.3 1.6 2.3 2.8 2.8l1.2-1 2 2-1.2 1.6c-3.4-.3-6.9-3.8-7.2-7.2z" fill="var(--blue)"/></svg>
        <svg viewBox="0 0 22 22" aria-label="website"><circle cx="11" cy="11" r="10" fill="none" stroke="var(--blue)" stroke-width="2"/><circle cx="11" cy="11" r="5.5" fill="none" stroke="var(--blue)" stroke-width="1.4"/><path d="M5.5 11h11M11 5.5c-2.5 3-2.5 8 0 11M11 5.5c2.5 3 2.5 8 0 11" fill="none" stroke="var(--blue)" stroke-width="1.2"/></svg>
        <svg viewBox="0 0 22 22" aria-label="email"><circle cx="11" cy="11" r="10" fill="none" stroke="var(--blue)" stroke-width="2"/><rect x="6" y="7.5" width="10" height="7" fill="var(--blue)"/><path d="M6 7.5l5 4 5-4" fill="none" stroke="var(--card)" stroke-width="1.2"/></svg>
      </div>
    </div>

    <p class="contact">
      (555)417-9382<br>
      www.cedarhollowmixdj.example<br>
      dario@cedarhollowmixdj.example
    </p>

    <div class="divider divider--social">
      <div class="icon-row">
        <svg viewBox="0 0 22 22" aria-hidden="true"><circle cx="11" cy="11" r="10" fill="var(--green)"/></svg>
        <svg viewBox="0 0 22 22" aria-hidden="true"><circle cx="11" cy="11" r="10" fill="var(--green)"/></svg>
        <svg viewBox="0 0 22 22" aria-hidden="true"><circle cx="11" cy="11" r="10" fill="var(--green)"/></svg>
      </div>
    </div>
    <p class="handle">@chmixdj</p>
  </section>

  <section class="card card--back">
    <div class="back-pattern" role="img" aria-label="Faint repeating pattern of the company mark in dark tones"></div>
    <p class="services">DJ<br>Photo Booth<br>Event Lighting<br>LED Robot</p>
  </section>
</main>
</body>
</html>
```